Brightfield Program (8 x 8) to be posted on Chatterbox, Quipster & Snapgrove

YOUR NEW HOME PURCHASE IS BRIGHTFIELD
with the
LBQ BRIGHTFIELD 2.0 PROGRAM
* Up to 5% Assistance with 640 Score
* Up to 6% Assistance with 660 Score
* Also 6% Seller Help Allowed
Call to be Pre-Qualified Today!
(800) 555-0147
Larkmoor Financial Services, Inc.
4120 Quarrelton Road, Ellicott City, MD 21987
www.larkmoorhomes-demo.com
NMLS #318764

```html
<!DOCTYPE html>
<html lang="en">
<head>
<meta charset="utf-8">
<title>Brightfield Program Post</title>
<link href="https://fonts.googleapis.com/css2?family=Oswald:wght@500;700&family=Roboto+Condensed:wght@400;700&family=Great+Vibes&display=swap" rel="stylesheet">
<style>
  :root{
    --blue:#0f5ea8;
    --blue-dark:#0a4a86;
    --ink:#111111;
    --white:#ffffff;
    --page:#eeeeee;
    --photo-a:#c9b29a;
    --photo-b:#7d5a44;
  }
  *{box-sizing:border-box;margin:0;padding:0}
  html,body{width:1200px;height:2360px;overflow:hidden;background:var(--page)}
  .post{
    position:absolute;left:48px;top:628px;width:1104px;height:1104px;
    background:var(--white);overflow:hidden;
    font-family:"Roboto Condensed",Arial,sans-serif;
    box-shadow:0 2px 10px rgba(0,0,0,.15);
  }
  .brand{
    position:absolute;left:30px;top:40px;display:flex;align-items:center;gap:14px;
    font-family:"Roboto Condensed",Arial,sans-serif;font-weight:700;
    font-size:22px;color:var(--blue);width:280px;line-height:1.15;
  }
  .brand .mark{width:54px;height:54px;background:var(--blue);flex:none}
  .headline-top{
    position:absolute;left:580px;top:30px;width:504px;height:62px;
    background:var(--blue);color:var(--white);
    font-family:"Oswald",Arial,sans-serif;font-weight:500;font-size:34px;
    display:flex;align-items:center;justify-content:center;letter-spacing:.5px;
  }
  .headline-main{
    position:absolute;left:580px;top:90px;width:504px;text-align:center;
    font-family:"Oswald",Arial,sans-serif;font-weight:700;font-size:76px;
    color:var(--blue);line-height:1.05;white-space:nowrap;
  }
  .headline-with{
    position:absolute;right:24px;top:176px;display:flex;align-items:center;gap:10px;
    font-family:"Great Vibes",cursive;font-size:36px;color:var(--ink);
  }
  .headline-with::before{content:"";width:150px;height:2px;background:var(--ink)}
  .photo{
    position:absolute;left:0;top:222px;width:1104px;height:500px;
    background:linear-gradient(135deg,var(--photo-a),var(--photo-b));
  }
  .rule{position:absolute;left:70px;top:214px;width:840px;height:10px;background:var(--blue)}
  .program-title{
    position:absolute;left:0;top:636px;width:1104px;text-align:center;
    font-family:"Oswald",Arial,sans-serif;font-weight:700;font-size:50px;
    color:var(--white);text-shadow:0 2px 6px rgba(0,0,0,.6);
  }
  .perks{position:absolute;left:20px;top:738px;display:flex;gap:14px}
  .perk{
    width:172px;height:172px;border-radius:50%;background:var(--blue);
    border:5px solid var(--white);box-shadow:0 0 0 3px var(--blue);
    color:var(--white);text-align:center;display:flex;flex-direction:column;
    justify-content:center;line-height:1.05;
  }
  .perk strong{font-family:"Oswald",Arial,sans-serif;font-size:34px;font-weight:700}
  .perk span{font-size:18px;font-weight:700;text-transform:uppercase}
  .cta{position:absolute;left:630px;top:764px;width:450px}
  .cta-label{
    font-family:"Oswald",Arial,sans-serif;font-weight:700;font-size:28px;
    color:var(--ink);text-align:right;white-space:nowrap;line-height:1.2;
  }
  .cta-phone{
    margin-top:14px;height:72px;background:var(--blue);color:var(--white);
    display:flex;align-items:center;justify-content:center;gap:14px;
    font-family:"Oswald",Arial,sans-serif;font-weight:700;font-size:46px;
    line-height:1;white-space:nowrap;
  }
  .thumbs{position:absolute;left:20px;top:930px;display:flex;gap:12px;align-items:center}
  .thumb{width:166px;height:112px;background:linear-gradient(135deg,#b9c6d3,#6c7f8f)}
  .thumb:nth-child(2){background:linear-gradient(135deg,#d9c2a8,#8a6a52)}
  .thumb:nth-child(3){background:linear-gradient(135deg,#cdb8a6,#6e5142)}
  .thumb:nth-child(4){background:linear-gradient(135deg,#dccfc0,#9a7a62)}
  .thumb:nth-child(5){background:linear-gradient(135deg,#b7c3b0,#a33a33)}
  .badge{width:150px;text-align:center;font-size:14px;font-weight:700;color:var(--ink)}
  .badge .shape{width:84px;height:84px;background:var(--ink);margin:0 auto 6px}
  .footer{
    position:absolute;left:0;bottom:0;width:1104px;height:56px;background:var(--ink);
    color:var(--white);display:flex;align-items:center;justify-content:space-between;
    padding:0 24px;font-size:22px;font-weight:700;white-space:nowrap;
  }
</style>
</head>
<body>
  <main class="post">
    <div class="brand"><span class="mark"></span>Larkmoor Financial Services, Inc.</div>

    <div class="headline-top">YOUR NEW HOME PURCHASE</div>
    <div class="headline-main">IS BRIGHTFIELD</div>
    <div class="headline-with">With the</div>

    <div class="photo" role="img" aria-label="Smiling family of four playing with moving boxes in their new home"></div>
    <div class="rule"></div>
    <h1 class="program-title">LBQ BRIGHTFIELD 2.0 PROGRAM</h1>

    <div class="perks">
      <div class="perk"><strong>UP TO 5%</strong><span>Assistance with<br>640 Score</span></div>
      <div class="perk"><strong>UP TO 6%</strong><span>Assistance with<br>660 Score</span></div>
      <div class="perk"><strong>ALSO 6%</strong><span>Seller help<br>allowed</span></div>
    </div>

    <div class="cta">
      <p class="cta-label">CALL TO BE PRE-QUALIFIED TODAY!</p>
      <div class="cta-phone">
        <svg width="40" height="40" viewBox="0 0 24 24" aria-hidden="true"><path fill="#fff" d="M6.6 10.8a15.2 15.2 0 0 0 6.6 6.6l2.2-2.2c.3-.3.7-.4 1-.2 1.1.4 2.3.6 3.6.6.6 0 1 .4 1 1V20c0 .6-.4 1-1 1A17 17 0 0 1 3 4c0-.6.4-1 1-1h3.5c.6 0 1 .4 1 1 0 1.3.2 2.5.6 3.6.1.3 0 .7-.2 1z"/></svg>
        (800) 555-0147
      </div>
    </div>

    <div class="thumbs">
      <div class="thumb" role="img" aria-label="House exterior with front door"></div>
      <div class="thumb" role="img" aria-label="Couple reviewing paperwork"></div>
      <div class="thumb" role="img" aria-label="Family celebrating at home"></div>
      <div class="thumb" role="img" aria-label="Couple holding house keys"></div>
      <div class="thumb" role="img" aria-label="Home with for sale sign"></div>
      <div class="badge"><div class="shape"></div>NMLS #318764</div>
    </div>

    <footer class="footer">
      <span>Larkmoor Financial Services, Inc. 4120 Quarrelton Road, Ellicott City, MD 21987</span>
      <span>www.larkmoorhomes-demo.com</span>
    </footer>
  </main>
</body>
</html>
```